Plimbo advertising imagery for a 13.28kW solar system

Project Overview:
We are thrilled to announce a limited-time offer on our top-of-the-line 13.28kW Solar System! This Plimbo ad campaign aims to generate excitement and interest among homeowners and businesses looking to harness the power of solar energy. The special offer includes a competitively priced 13.28kW solar system starting from $5800, fully installed, and an exclusive free upgrade to the Velmarq 10kW 1 Phase inverter for a limited two-week period.

Target Audience:
Our target audience consists of environmentally conscious homeowners, small to medium-sized businesses, and those seeking to reduce their energy bills and carbon footprint. We will be focusing on customers in [your service area location] or nearby regions, aged between 25 to 65 years old.

Key Message:
The advertisement should convey the following key messages:

"Go Solar and Save Big on Your Energy Bills!"
"Upgrade to the Powerful Velmarq Inverter for Free - Limited Time Only!"
"High-Performance 13.28kW Solar System Fully Installed from $5800."
"Harness Clean and Renewable Energy to Power Your Home or Business."
Design Requirements:

Dimensions: The advertisement should comply with Plimbo's recommended ad dimensions (e.g., 1200 x 628 pixels).
Branding: Incorporate our company logo and colors (Logo attached).
Visuals: Use eye-catching images or animations that showcase solar panels, clean energy, and happy customers enjoying the benefits of solar power.
Call-to-Action (CTA): Include a prominent CTA button, such as "Get a Quote," "Limited Time Offer - Act Now!" or "Learn More."
Text: Keep the text clear, concise, and persuasive, highlighting the savings, eco-friendliness, and exclusive offer.
Pricing Details: Clearly mention the starting price of the 13.28kW solar system and emphasize the free upgrade to the Velmarq 10kW 1 Phase inverter.
Trust Signals: Incorporate any relevant awards, certifications, or customer testimonials to build trust and credibility.
Countdown Timer (Optional): Consider adding a countdown timer to create a sense of urgency and remind viewers about the limited-time offer.
Additional Information:

Include the following contact information: Website URL, phone number, and email address.
The advertisement should comply with Plimbo's advertising guidelines and policies.
Prominently display the duration of the offer: "Two Weeks Only - Act Fast!"

Target Market(s)

Industry/Entity Type

Solar Energy

Colors
0054AA
0677BA
7BADD7
CADEEF
E8F1F8

Requirements
Must have
• Key Message: The advertisement should convey the following key messages: "Go Solar and Save Big on Your Energy Bills!" "Upgrade to the Powerful Velmarq Inverter for Free - Limited Time Only!" "High-Performance 13.28kW Solar System Fully Installed from $5800." "Harness Clean and Renewable Energy to Power Your Home or Business."
Nice to have
• Must have picture of solar panels and the Velmarq 10kW 1 Phase inverter

```html
<!DOCTYPE html>
<html lang="en">
<head>
<meta charset="utf-8">
<title>Corvale Energy – Go Solar Offer</title>
<link rel="stylesheet" href="https://fonts.googleapis.com/css2?family=Montserrat:wght@400;500;600;700;800&display=swap">
<style>
  :root {
    --sky-deep: #1f5f9c;
    --sky-mid: #4f8ec4;
    --cloud: #dfe8f1;
    --panel-dark: #1d2d4a;
    --panel-mid: #3b5279;
    --brand-red: #c01f2f;
    --bar-red: rgba(150, 24, 36, 0.88);
    --offer-red: rgba(192, 31, 47, 0.94);
    --badge-navy: #2c3345;
    --white: #ffffff;
  }
  * { margin: 0; padding: 0; box-sizing: border-box; }
  html, body { width: 1200px; height: 628px; overflow: hidden; background: #ffffff; }
  body { font-family: "Montserrat", Arial, sans-serif; color: var(--white); }

  .ad { position: relative; width: 1200px; height: 628px; overflow: hidden; }

  .hero-photo {
    position: absolute; inset: 0;
    background:
      radial-gradient(ellipse 360px 180px at 190px 270px, rgba(236,242,248,0.9), rgba(236,242,248,0) 70%),
      radial-gradient(ellipse 420px 160px at 560px 300px, rgba(230,238,246,0.85), rgba(230,238,246,0) 70%),
      radial-gradient(ellipse 300px 200px at 820px 420px, rgba(225,234,244,0.7), rgba(225,234,244,0) 70%),
      linear-gradient(150deg, rgba(0,0,0,0) 55%, var(--panel-mid) 62%, var(--panel-dark) 80%),
      linear-gradient(180deg, var(--sky-deep) 0%, var(--sky-mid) 45%, var(--cloud) 100%);
  }

  .headline, .urgency-badge { position: absolute; left: 0; top: 0; width: 1200px; height: 628px; }
  .headline text, .urgency-badge text { font-family: "Montserrat", Arial, sans-serif; fill: var(--white); }
  .headline-go    { font-size: 265px; font-weight: 500; }
  .headline-solar { font-size: 66px; font-weight: 700; }
  .headline-save  { font-size: 50px; font-weight: 600; }
  .headline-amp   { font-size: 50px; font-weight: 400; }
  .headline .headline-amp { fill: none; stroke: var(--white); stroke-width: 1.4; }
  .headline-big   { font-size: 78px; font-weight: 700; }
  .headline-bills { font-size: 44px; font-weight: 600; }
  .headline-bills tspan { font-weight: 800; }

  .urgency-number { font-size: 96px; font-weight: 800; }
  .urgency-weeks  { font-size: 14px; font-weight: 800; }
  .urgency-badge .urgency-weeks { stroke: var(--badge-navy); stroke-width: 5px; paint-order: stroke; stroke-linejoin: round; }
  .urgency-cta    { font-size: 24px; font-weight: 700; }
  .urgency-cta tspan { font-size: 36px; font-weight: 800; }

  .brand-panel {
    position: absolute; left: 742px; top: 0; width: 353px; height: 240px;
    background: var(--brand-red);
    display: flex; align-items: center; justify-content: center; gap: 16px;
  }
  .brand-square { width: 52px; height: 52px; background: var(--white); }
  .brand-name { font-size: 40px; font-weight: 700; line-height: 1.05; letter-spacing: 1px; }

  .offer-panel {
    position: absolute; left: 472px; top: 405px; width: 728px; height: 95px;
    background: var(--offer-red);
    padding: 8px 0 0 18px;
    font-size: 15px; font-weight: 700; line-height: 29px; white-space: nowrap;
  }
  .offer-panel strong { font-size: 19px; font-weight: 800; }

  .contact-bar {
    position: absolute; left: 0; top: 543px; width: 1200px; height: 55px;
    background: var(--bar-red);
    display: flex; align-items: center; font-weight: 700; white-space: nowrap;
  }
  .contact-phone { position: absolute; left: 50px; font-size: 20px; }
  .contact-web   { position: absolute; left: 398px; font-size: 26px; }
  .contact-email { position: absolute; left: 846px; font-size: 20px; }
</style>
</head>
<body>
<main class="ad">
  <div class="hero-photo" role="img" aria-label="Blue sky with white clouds above rows of solar panels"></div>

  <svg class="headline" viewBox="0 0 1200 628" width="1200" height="628" role="heading" aria-level="1" aria-label="Go Solar, Save and Big on Your Energy Bills">
    <text class="headline-go" x="92" y="285" textLength="385" lengthAdjust="spacingAndGlyphs">GO</text>
    <text class="headline-solar" x="405" y="215" textLength="215" lengthAdjust="spacingAndGlyphs">SOLAR</text>
    <text class="headline-save" x="490" y="270" textLength="130" lengthAdjust="spacingAndGlyphs">Save</text>
    <text class="headline-amp" x="446" y="322" textLength="42" lengthAdjust="spacingAndGlyphs">&amp;</text>
    <text class="headline-big" x="488" y="345" textLength="132" lengthAdjust="spacingAndGlyphs">BIG</text>
    <text class="headline-bills" x="488" y="398" textLength="477" lengthAdjust="spacingAndGlyphs">on Your <tspan>Energy Bills</tspan></text>
  </svg>

  <svg class="urgency-badge" viewBox="0 0 1200 628" width="1200" height="628" aria-label="Two weeks only, act now">
    <polygon transform="translate(167 283) scale(1.136)" fill="var(--badge-navy)" points="220,110 196.3,127.2 211.6,152.1 183.1,158.9 187.8,187.8 158.9,183.1 152.1,211.6 127.2,196.3 110,220 92.8,196.3 67.9,211.6 61.1,183.1 32.2,187.8 36.9,158.9 8.4,152.1 23.7,127.2 0,110 23.7,92.8 8.4,67.9 36.9,61.1 32.2,32.2 61.1,36.9 67.9,8.4 92.8,23.7 110,0 127.2,23.7 152.1,8.4 158.9,36.9 187.8,32.2 183.1,61.1 211.6,67.9 196.3,92.8"/>
    <text class="urgency-number" x="295" y="425" text-anchor="middle">2</text>
    <text class="urgency-weeks" x="290" y="391" text-anchor="middle">WEEKS ONLY</text>
    <text class="urgency-cta" x="218" y="463" textLength="144" lengthAdjust="spacingAndGlyphs">Act <tspan>Now!</tspan></text>
  </svg>

  <div class="brand-panel">
    <span class="brand-square" aria-hidden="true"></span>
    <span class="brand-name">CORVALE<br>ENERGY</span>
  </div>

  <div class="offer-panel">
    <div>Upgrade to the Powerful Velmarq Inverter for <strong>Free</strong> - Limited Time Only</div>
    <div>High-Performance <strong>13.28kW</strong> Solar System Fully Installed from <strong>$5800</strong></div>
    <div>Harness Clean and Renewable Energy to Power Your Home or Business</div>
  </div>

  <div class="contact-bar">
    <span class="contact-phone">CALL US: (07) 3000 4182</span>
    <span class="contact-web">www.corvaleenergy.com.au</span>
    <span class="contact-email">info@corvaleenergy.com.au</span>
  </div>
</main>
</body>
</html>
```